Copper & Wren Labels*

Hello :) I am needing labels for my herbal tea/petal product. I am a small producer for the local restaurants (edible flowers/micro herbs & dried product). I am hoping to sell the dried product online. It will be sold in batches as it is ready so quite small/boutique and the label needs to be somewhat generic for the range of produce I make.
Feels: no/minimal plastic, product is in a reusable mason jar, we use organic/regenerative principles from soil health to end product. Treading gently on the land. High quality i.e only fresh hand picked leaf tips for the tea.

```html
<!DOCTYPE html>
<html lang="en">
<head>
<meta charset="utf-8">
<title>Copper &amp; Wren Labels</title>
<link rel="stylesheet" href="https://fonts.googleapis.com/css2?family=Barlow:wght@400;500;600&family=Playfair+Display:wght@400&family=Libre+Caslon+Text:wght@400&display=swap">
<style>
  :root {
    --leaf-green: #48a942;
    --label-white: #ffffff;
    --ink-green: #3fa33a;
    --earth-brown: #8a5a3a;
    --rule-green: #7cc377;
  }
  * { margin: 0; padding: 0; box-sizing: border-box; }
  html, body { width: 1200px; height: 1200px; overflow: hidden; }
  body {
    background: var(--leaf-green);
    display: flex;
    align-items: flex-start;
    justify-content: center;
    gap: 55px;
    padding-top: 300px;
  }
  .label {
    background: var(--label-white);
    width: 320px;
    color: var(--ink-green);
    display: flex;
    flex-direction: column;
    align-items: center;
  }
  .label--tall { height: 560px; padding-top: 72px; }
  .label--front { height: 380px; padding-top: 40px; }
  .label--details { height: 320px; padding: 42px 30px; }

  .brand { display: flex; flex-direction: column; align-items: center; }
  .brand__dot { border-radius: 50%; background: var(--ink-green); }
  .brand__name {
    font-family: "Barlow", sans-serif;
    font-weight: 600;
    color: var(--ink-green);
    letter-spacing: -0.5px;
  }
  .label--tall .brand__dot { width: 102px; height: 102px; }
  .label--tall .brand__name { font-size: 32px; margin-top: 4px; }
  .label--front .brand__dot { width: 74px; height: 74px; }
  .label--front .brand__name { font-size: 23px; margin-top: 2px; }

  .product {
    font-family: "Playfair Display", serif;
    text-align: center;
    color: var(--ink-green);
    line-height: 0.95;
  }
  .product__main { display: block; letter-spacing: -1px; }
  .product__amp { display: block; }
  .label--tall .product { margin-top: 30px; }
  .label--tall .product__main { font-size: 64px; }
  .label--tall .product__amp { font-size: 50px; margin-top: 4px; }
  .label--front .product { margin-top: 18px; }
  .label--front .product__main { font-size: 48px; }
  .label--front .product__amp { font-size: 36px; margin-top: 2px; }

  .tagline, .origin {
    font-family: "Libre Caslon Text", serif;
    text-transform: uppercase;
    text-align: center;
    letter-spacing: 1.2px;
  }
  .tagline { color: var(--earth-brown); }
  .origin { color: var(--ink-green); line-height: 1.55; }
  .label--tall .tagline { font-size: 12.5px; margin-top: 38px; }
  .label--tall .origin { font-size: 11px; margin-top: 26px; }
  .label--front .tagline { font-size: 9.5px; margin-top: 28px; }
  .label--front .origin { font-size: 8px; margin-top: 18px; }

  .details {
    width: 100%;
    border: 1px solid var(--rule-green);
    border-collapse: collapse;
    font-family: "Barlow", sans-serif;
    color: var(--ink-green);
  }
  .details td { border-top: 1px solid var(--rule-green); vertical-align: middle; }
  .details__title { font-size: 16px; font-weight: 500; height: 47px; padding-left: 11px; }
  .details__key { font-size: 15px; width: 91px; height: 47px; padding-left: 7px; border-right: 1px solid var(--rule-green); }
  .details__value { font-size: 9.5px; line-height: 1.35; padding-left: 9px; }
  .details__farm { font-size: 15px; line-height: 1.3; height: 46px; padding-left: 8px; }
</style>
</head>
<body>
  <section class="label label--tall">
    <div class="brand">
      <span class="brand__dot"></span>
      <span class="brand__name">Fernhollow</span>
    </div>
    <h1 class="product"><span class="product__main">COPPER</span><span class="product__amp">&amp; WREN</span></h1>
    <p class="tagline">Grown, harvested and dried</p>
    <p class="origin">Chemical free on our<br>farm in Bracken Valley</p>
  </section>

  <section class="label label--front">
    <div class="brand">
      <span class="brand__dot"></span>
      <span class="brand__name">Fernhollow</span>
    </div>
    <h2 class="product"><span class="product__main">COPPER</span><span class="product__amp">&amp; WREN</span></h2>
    <p class="tagline">Grown, harvested and dried</p>
    <p class="origin">Chemical free on our<br>farm in Bracken Valley</p>
  </section>

  <section class="label label--details">
    <table class="details">
      <tr><td class="details__title" colspan="2">SINGLE ORIGIN HERBAL TEA ETC.</td></tr>
      <tr><td class="details__key">Leaf Base</td><td class="details__value">Lemon Verbena<br>Mint<br>Agastache</td></tr>
      <tr><td class="details__key">Petals</td><td class="details__value"></td></tr>
      <tr><td class="details__key">Batch</td><td class="details__value"></td></tr>
      <tr><td class="details__farm" colspan="2">Willow Bend<br>Victoria Australia</td></tr>
    </table>
  </section>
</body>
</html>
```